Business Card Design

We need a business card design for a new company based in Melbourne Australia. We are financial broker in finance industry. We provide a wide range of finance solutions to our clients including home loans, commercial loans, business facilities, car loans, equipment loans, invoice finance, etc. The company name is from director's personal name. We would like to have a new company logo that includes KT.

Industry/Entity Type

Business

Contact Information for Business Card

company name: KT & Co Finance Pty Ltd
person's name: Kenneth Tollard
role: Managing Director
Mobile: 0417 638 294
fax: 03 9561 2047
Email: kenneth.tollard@ktcofinance.example
Address: Suite 4/718 Marlow Avenue Ferndale East Vic 3187
Credit Licence No.: 382917

```html
<!DOCTYPE html>
<html lang="en">
<head>
<meta charset="utf-8">
<title>KT &amp; Co Finance Pty Ltd — Business Card</title>
<link rel="stylesheet" href="https://fonts.googleapis.com/css2?family=Open+Sans:wght@400;600;700;800&display=swap">
<style>
  :root {
    --navy: #26207a;
    --navy-deep: #1c175e;
    --paper: #f7f7f7;
    --grey-text: #9a9aa2;
    --grey-icon: #a6a6ad;
    --backdrop: #e6e4e0;
    --white: #ffffff;
  }
  * { margin: 0; padding: 0; box-sizing: border-box; }
  html, body { width: 1200px; height: 780px; overflow: hidden; }
  body {
    background: var(--backdrop);
    font-family: "Open Sans", Arial, sans-serif;
  }
  .canvas {
    width: 1200px; height: 780px;
    display: flex; align-items: center; justify-content: center; gap: 40px;
  }
  .card {
    width: 540px; height: 320px;
    position: relative; overflow: hidden;
    box-shadow: 0 6px 18px rgba(0,0,0,.18);
  }

  /* Front */
  .card-front { background: var(--paper); }
  .brand-block {
    position: absolute; left: 34px; top: 0; width: 200px; height: 262px;
    display: flex; align-items: center; gap: 10px;
  }
  .brand-mark { width: 14px; height: 14px; background: var(--navy); flex: none; }
  .brand-name {
    color: var(--navy); font-weight: 700; font-size: 21px; line-height: 1.2;
  }
  .divider {
    position: absolute; left: 262px; top: 40px; width: 1px; height: 180px;
    background: var(--navy); opacity: .55;
  }
  .contact-block { position: absolute; left: 284px; top: 44px; right: 20px; }
  .person-name {
    color: var(--navy); font-weight: 800; font-size: 19px; letter-spacing: .2px;
  }
  .person-role { color: var(--grey-text); font-size: 13px; margin-top: -2px; }
  .contact-list { list-style: none; margin-top: 28px; }
  .contact-list li {
    display: flex; align-items: center; gap: 8px;
    color: var(--navy-deep); font-size: 12.5px; line-height: 22px;
  }
  .contact-icon { width: 16px; height: 16px; flex: none; }
  .licence { color: var(--grey-text); font-size: 12.5px; margin-top: 6px; }
  .address-band {
    position: absolute; left: 0; right: 0; bottom: 0; height: 58px;
    background: var(--navy);
    display: flex; align-items: center; justify-content: flex-end; padding-right: 26px;
    color: var(--white); font-size: 14.5px;
  }

  /* Back */
  .card-back {
    background: radial-gradient(ellipse at 45% 40%, #2d2790 0%, var(--navy) 55%, var(--navy-deep) 100%);
    display: flex; align-items: center; justify-content: center; gap: 14px;
  }
  .card-back .brand-mark { background: var(--white); width: 18px; height: 18px; }
  .card-back .brand-name { color: var(--white); font-size: 30px; }
</style>
</head>
<body>
  <main class="canvas">
    <section class="card card-front" aria-label="Business card front">
      <div class="brand-block">
        <span class="brand-mark"></span>
        <span class="brand-name">KT &amp; Co Finance Pty Ltd</span>
      </div>
      <div class="divider"></div>
      <div class="contact-block">
        <p class="person-name">KENNETH TOLLARD</p>
        <p class="person-role">Managing Director</p>
        <ul class="contact-list">
          <li>
            <svg class="contact-icon" viewBox="0 0 16 16" aria-hidden="true">
              <rect width="16" height="16" rx="2" fill="var(--grey-icon)"/>
              <rect x="5" y="2.5" width="6" height="11" rx="1" fill="none" stroke="#fff" stroke-width="1.2"/>
              <circle cx="8" cy="11.5" r=".7" fill="#fff"/>
            </svg>
            0417 638 294
          </li>
          <li>
            <svg class="contact-icon" viewBox="0 0 16 16" aria-hidden="true">
              <rect width="16" height="16" rx="2" fill="var(--grey-icon)"/>
              <rect x="3" y="6" width="10" height="6" rx="1" fill="none" stroke="#fff" stroke-width="1.2"/>
              <rect x="5" y="3" width="6" height="3" fill="none" stroke="#fff" stroke-width="1.1"/>
            </svg>
            03 9561 2047
          </li>
          <li>
            <svg class="contact-icon" viewBox="0 0 16 16" aria-hidden="true">
              <rect width="16" height="16" rx="2" fill="var(--grey-icon)"/>
              <rect x="3" y="4.5" width="10" height="7" fill="none" stroke="#fff" stroke-width="1.2"/>
              <path d="M3 4.5 L8 9 L13 4.5" fill="none" stroke="#fff" stroke-width="1.2"/>
            </svg>
            kenneth.tollard@ktcofinance.example
          </li>
        </ul>
        <p class="licence">Licence No.: 382917</p>
      </div>
      <div class="address-band">Suite 4/718 Marlow Avenue Ferndale East Vic 3187</div>
    </section>

    <section class="card card-back" aria-label="Business card back">
      <span class="brand-mark"></span>
      <span class="brand-name">KT &amp; Co Finance Pty Ltd</span>
    </section>
  </main>
</body>
</html>
```